Zestra Design Prize - $10,000 tablet app design contest, Magazine Category

Zestra is a marketplace for Slatepad App Templates (similar to BlogForge templates). We want you to design an app template for sale in our marketplace which targets B2B or B2C Magazine Apps (Slatepad Apps created for examples such as Alumni magazine, employee magazine, sports magazine, fashion magazine etc).

It’s up to you to create pages or features for the App Template that you think are appropriate. Creativity will be rewarded! Here are some example pages or features that you could create:

• Contents
• Editor’s letter
• Event calendar
• News page
• Feature article
• Business articles
• Social media integration
• Animations and video

Your design should be Vibrant, Engaging and Contemporary. If you have an Slatepad, download Zestra Viewer and download template examples in the download tab.

Your entry must include:
• A brief description of your template
• Preview images of all pages of your template

Attached to this project are free templates to help you get started with your design. We have included:
1. A free portfolio template for designers/photographers
2. Icons and artwork to use in your template
3. Blank pages template
4. Form template
5. Video ad template

If you are selected as a finalist you will be required to submit an .oproject file containing:
• Your InDesign source files
• Preview images of your template
• All creative / stock assets used in the template (animations, video etc.)
• A text file with instructions on how to update the template
• A metadata .txt file containing template details and your information

How to enter:
1. Register at Marketplace and view the instructions under the welcome message https://marketplace.zestrahub.example/welcome
2. Download Zestra Editor: https://support.zestrahub.example/entries/48175093-zestra-editor
3. Use the free templates provided in this brief to create your designs and submit to ArtHive

Reason: Due to the Christmas break we are extending the deadline of our competition. Thank you for time and effort - I will be providing feedback over the next couple of days! Best wishes, Lavinia

Hi All,

I have received many screenshots with some great designs! I just wanted to clarify that you are designing Zestra app templates including Zestra features and not just page designs?

Read Tips for First Time Zestrans to guide you through the template creation process

Before you start designing templates for Zestra Marketplace

·       Read the Quality Standards

·       Read the Copyright Information 

·       Use the Template Quality Checklist to ensure your template follows our guidelines. 

What should my project file contain?

·       A folder containing your source files, e.g. InDesign. This must be named Source.

·       The Zestra content files. This must be named Bundle.

·       Instructions, explaining to a customer how to use your template.

Best wishes,

Lavinia

Reason: We are extending the competition by 7 days to give you more time!

Reason: We have received 3 complete designs for this contest so we are extending the deadline for 7 days Best wishes, Lavinia

Target Market(s)

Entrepreneurs who wish to create Slatepad Apps by using our App design templates.

Industry/Entity Type

Fashion

Requirements
Must have
• You will need Zestra Editor to open the .oproject files attached to this brief. Get it here: https://support.zestrahub.example/entries/48175093-zestra-editor
Should not have
• • Low quality, fuzzy or blurry images
• Any stock images or content which you do not own the rights to
• Any material which could be considered inappropriate or offensive

```html
<!DOCTYPE html>
<html lang="en">
<head>
<meta charset="utf-8">
<title>Events – Zestra Magazine Template</title>
<link rel="stylesheet" href="https://fonts.googleapis.com/css2?family=Exo+2:wght@400;600;700&family=Oswald:wght@700&family=Open+Sans:wght@400;600&display=swap">
<style>
  :root {
    --status-bg: #000000;
    --status-text: #e6e6e6;
    --header-top: #12a0de;
    --header-bottom: #0076b8;
    --header-title: #1b4e78;
    --header-edge: #0a5f93;
    --sub-top: #e4e1db;
    --sub-bottom: #a9a59c;
    --sub-text: #2a2a2a;
    --row-bg: #f3f3f3;
    --row-line: #d2d2d2;
    --text-dark: #222222;
    --time-red: #e8003d;
    --btn-top: #3fb9f0;
    --btn-bottom: #0a86cc;
    --btn-text: #e9f6fd;
    --footer-top: #f4f5f6;
    --footer-bottom: #c9ccd0;
  }
  * { box-sizing: border-box; margin: 0; padding: 0; }
  html, body { width: 948px; height: 1200px; overflow: hidden; background: #ffffff; }
  .app { width: 948px; height: 1200px; display: flex; flex-direction: column; background: var(--row-bg); }

  .status-bar {
    height: 32px; background: var(--status-bg); color: var(--status-text);
    display: flex; align-items: center; justify-content: space-between;
    padding: 0 12px; font: 600 19px/1 "Open Sans", sans-serif; position: relative;
  }
  .status-bar .device { display: flex; align-items: center; gap: 8px; }
  .status-bar .clock { position: absolute; left: 50%; transform: translateX(-50%); }
  .status-bar .indicators { display: flex; align-items: center; gap: 10px; }

  .app-header {
    height: 100px; border-bottom: 3px solid var(--header-edge);
    background: linear-gradient(var(--header-top), var(--header-bottom));
    display: flex; align-items: center; justify-content: center;
  }
  .app-header h1 {
    font: 700 58px/1 "Exo 2", sans-serif; color: var(--header-title);
    letter-spacing: 1px; text-shadow: 0 1px 0 rgba(255,255,255,.35);
  }

  .section-bar {
    height: 60px; background: linear-gradient(var(--sub-top), var(--sub-bottom));
    border-bottom: 1px solid #8d8a83; display: flex; align-items: center; padding-left: 21px;
  }
  .section-bar h2 { font: 700 33px/1 "Oswald", sans-serif; color: var(--sub-text); letter-spacing: .5px; }

  .event-list { list-style: none; flex: 1; display: flex; flex-direction: column; }
  .event {
    flex: 1; border-bottom: 1px solid var(--row-line);
    display: flex; padding: 22px 21px 0;
  }
  .event:last-child { border-bottom: none; }
  .event-meta { width: 294px; font: 400 19.5px/30px "Exo 2", sans-serif; color: var(--text-dark); }
  .event-meta .time { color: var(--time-red); }
  .event-body { flex: 1; }
  .event-body p { font: 400 14.3px/21px "Open Sans", sans-serif; color: var(--text-dark); }
  .more-btn { display: block; margin-top: 8px; width: 62px; height: 36px; }

  .toolbar {
    height: 72px; border-top: 1px solid #b5b8bc;
    background: linear-gradient(var(--footer-top), var(--footer-bottom));
    display: flex; align-items: center; justify-content: space-between; padding: 0 32px 0 15px;
  }
  .pager { display: flex; gap: 4px; }
</style>
</head>
<body>
<div class="app">
  <div class="status-bar">
    <span class="device">Slatepad
      <svg width="24" height="18" viewBox="0 0 24 18" aria-hidden="true"><g fill="none" stroke="#e6e6e6" stroke-width="2.6" stroke-linecap="round"><path d="M2 6a14 14 0 0 1 20 0"/><path d="M6 10a8 8 0 0 1 12 0"/></g><circle cx="12" cy="14.5" r="2.2" fill="#e6e6e6"/></svg>
    </span>
    <span class="clock">4:20 PM</span>
    <span class="indicators">
      <svg width="16" height="16" viewBox="0 0 16 16" aria-hidden="true"><circle cx="8" cy="8" r="7" fill="#d0d0d0"/><path d="M8 3v5h4" stroke="#000" stroke-width="2" fill="none"/></svg>
      <svg width="34" height="16" viewBox="0 0 34 16" aria-hidden="true"><rect x="1" y="1" width="29" height="14" rx="2" fill="none" stroke="#e6e6e6" stroke-width="2"/><rect x="4" y="4" width="23" height="8" fill="#e6e6e6"/><rect x="31" y="5" width="3" height="6" fill="#e6e6e6"/></svg>
    </span>
  </div>

  <header class="app-header"><h1>EVENTS</h1></header>
  <div class="section-bar"><h2>LIST OF EVENTS</h2></div>

  <ul class="event-list">
    <li class="event">
      <div class="event-meta">12th January, 2013,<br>Verano Hall<br><span class="time">8.30 am-02.30 pm</span></div>
      <div class="event-body">
        <p>Lorem ipsum dolor sit amet, consectetur adipiscing elit. Donec aliquet est ut elit accumsan non convallis eros luctus. Ut condimentum sem in sem vulputate rhoncus.</p>
        <svg class="more-btn" viewBox="0 0 62 36" role="img" aria-label="More"><defs><linearGradient id="btnFill" x1="0" y1="0" x2="0" y2="1"><stop offset="0" stop-color="#3fb9f0"/><stop offset="1" stop-color="#0a86cc"/></linearGradient></defs><path d="M3 1h45l13 17-13 17H3a2 2 0 0 1-2-2V3a2 2 0 0 1 2-2z" fill="url(#btnFill)" stroke="#0b78b5"/><text x="26" y="23" text-anchor="middle" font-family="Open Sans, sans-serif" font-weight="600" font-size="14" fill="#e9f6fd">More</text></svg>
      </div>
    </li>
    <li class="event">
      <div class="event-meta">12th January, 2013,<br>Verano Hall<br><span class="time">8.30 am-02.30 pm</span></div>
      <div class="event-body">
        <p>Lorem ipsum dolor sit amet, consectetur adipiscing elit. Donec aliquet est ut elit accumsan non convallis eros luctus. Ut condimentum sem in sem vulputate rhoncus.</p>
        <svg class="more-btn" viewBox="0 0 62 36" role="img" aria-label="More"><path d="M3 1h45l13 17-13 17H3a2 2 0 0 1-2-2V3a2 2 0 0 1 2-2z" fill="url(#btnFill)" stroke="#0b78b5"/><text x="26" y="23" text-anchor="middle" font-family="Open Sans, sans-serif" font-weight="600" font-size="14" fill="#e9f6fd">More</text></svg>
      </div>
    </li>
    <li class="event">
      <div class="event-meta">12th January, 2013,<br>Verano Hall<br><span class="time">8.30 am-02.30 pm</span></div>
      <div class="event-body">
        <p>Lorem ipsum dolor sit amet, consectetur adipiscing elit. Donec aliquet est ut elit accumsan non convallis eros luctus. Ut condimentum sem in sem vulputate rhoncus.</p>
        <svg class="more-btn" viewBox="0 0 62 36" role="img" aria-label="More"><path d="M3 1h45l13 17-13 17H3a2 2 0 0 1-2-2V3a2 2 0 0 1 2-2z" fill="url(#btnFill)" stroke="#0b78b5"/><text x="26" y="23" text-anchor="middle" font-family="Open Sans, sans-serif" font-weight="600" font-size="14" fill="#e9f6fd">More</text></svg>
      </div>
    </li>
    <li class="event">
      <div class="event-meta">12th January, 2013,<br>Verano Hall<br><span class="time">8.30 am-02.30 pm</span></div>
      <div class="event-body">
        <p>Lorem ipsum dolor sit amet, consectetur adipiscing elit. Donec aliquet est ut elit accumsan non convallis eros luctus. Ut condimentum sem in sem vulputate rhoncus.</p>
        <svg class="more-btn" viewBox="0 0 62 36" role="img" aria-label="More"><path d="M3 1h45l13 17-13 17H3a2 2 0 0 1-2-2V3a2 2 0 0 1 2-2z" fill="url(#btnFill)" stroke="#0b78b5"/><text x="26" y="23" text-anchor="middle" font-family="Open Sans, sans-serif" font-weight="600" font-size="14" fill="#e9f6fd">More</text></svg>
      </div>
    </li>
    <li class="event">
      <div class="event-meta">12th January, 2013,<br>Verano Hall<br><span class="time">8.30 am-02.30 pm</span></div>
      <div class="event-body">
        <p>Lorem ipsum dolor sit amet, consectetur adipiscing elit. Donec aliquet est ut elit accumsan non convallis eros luctus. Ut condimentum sem in sem vulputate rhoncus.</p>
        <svg class="more-btn" viewBox="0 0 62 36" role="img" aria-label="More"><path d="M3 1h45l13 17-13 17H3a2 2 0 0 1-2-2V3a2 2 0 0 1 2-2z" fill="url(#btnFill)" stroke="#0b78b5"/><text x="26" y="23" text-anchor="middle" font-family="Open Sans, sans-serif" font-weight="600" font-size="14" fill="#e9f6fd">More</text></svg>
      </div>
    </li>
    <li class="event">
      <div class="event-meta">12th January, 2013,<br>Verano Hall<br><span class="time">8.30 am-02.30 pm</span></div>
      <div class="event-body">
        <p>Lorem ipsum dolor sit amet, consectetur adipiscing elit. Donec aliquet est ut elit accumsan non convallis eros luctus. Ut condimentum sem in sem vulputate rhoncus.</p>
        <svg class="more-btn" viewBox="0 0 62 36" role="img" aria-label="More"><path d="M3 1h45l13 17-13 17H3a2 2 0 0 1-2-2V3a2 2 0 0 1 2-2z" fill="url(#btnFill)" stroke="#0b78b5"/><text x="26" y="23" text-anchor="middle" font-family="Open Sans, sans-serif" font-weight="600" font-size="14" fill="#e9f6fd">More</text></svg>
      </div>
    </li>
    <li class="event">
      <div class="event-meta">12th January, 2013,<br>Verano Hall<br><span class="time">8.30 am-02.30 pm</span></div>
      <div class="event-body">
        <p>Lorem ipsum dolor sit amet, consectetur adipiscing elit. Donec aliquet est ut elit accumsan non convallis eros luctus. Ut condimentum sem in sem vulputate rhoncus.</p>
        <svg class="more-btn" viewBox="0 0 62 36" role="img" aria-label="More"><path d="M3 1h45l13 17-13 17H3a2 2 0 0 1-2-2V3a2 2 0 0 1 2-2z" fill="url(#btnFill)" stroke="#0b78b5"/><text x="26" y="23" text-anchor="middle" font-family="Open Sans, sans-serif" font-weight="600" font-size="14" fill="#e9f6fd">More</text></svg>
      </div>
    </li>
  </ul>

  <footer class="toolbar">
    <svg width="64" height="38" viewBox="0 0 64 38" role="img" aria-label="Home"><path d="M14 1h47a2 2 0 0 1 2 2v32a2 2 0 0 1-2 2H14L1 19z" fill="url(#btnFill)" stroke="#0b78b5"/><path d="M37 8l-14 12h4v10h7v-6h6v6h7V20h4z" fill="#ffffff"/></svg>
    <div class="pager">
      <svg width="38" height="38" viewBox="0 0 38 38" role="img" aria-label="Previous"><rect x="1" y="1" width="36" height="36" rx="2" fill="url(#btnFill)" stroke="#0b78b5"/><path d="M23 9l-10 10 10 10" fill="none" stroke="#fff" stroke-width="3"/></svg>
      <svg width="38" height="38" viewBox="0 0 38 38" role="img" aria-label="Next"><rect x="1" y="1" width="36" height="36" rx="2" fill="url(#btnFill)" stroke="#0b78b5"/><path d="M15 9l10 10-10 10" fill="none" stroke="#fff" stroke-width="3"/></svg>
    </div>
  </footer>
</div>
</body>
</html>
```